Letterhead for a German Distribution/Manufacturing Company

We need a professional Letterhead in a unique Design.
not to playful.
The Letterhead has to show show that we are a international company with headquater in Germany.
all details like adress, Vat Tax Number, Bank Accout, Eori, email, Company number has to be on the Letterhead.
for example use: VAT TAX DE5704168 Bank Account: Norrfeld Bank IBAN DE421705238ß310482 Swift: KOLV3154802 EORI 3041296587 Company Number: HRB 61508 Adress: VOLTRINA UG Amsel Strasse 7 Postal Code 04683 City Harzwalde Country: Germany Email: info@voltrina-example.com
the design can be colored but doesnt have to be
Industry/Entity Type
Manufacturing and international distribution
Requirements
Must have
- show that we are a international company with headquater in Germany. our company infos and logo

```html
<!DOCTYPE html>
<html lang="en">
<head>
<meta charset="utf-8">
<title>VOLTRINA Letterhead</title>
<link href="https://fonts.googleapis.com/css2?family=Montserrat:wght@400;500;700&family=Lobster&display=swap" rel="stylesheet">
<style>
  :root {
    --backdrop: #ececec;
    --paper: #ffffff;
    --band: #585858;
    --ink: #2d3142;
    --text: #333333;
    --accent: #e8473e;
    --tint: #efefef;
    --tint-strong: #e0e0e0;
  }
  html, body {
    margin: 0;
    padding: 0;
    width: 1200px;
    height: 1200px;
    overflow: hidden;
    background: var(--backdrop);
    font-family: "Montserrat", sans-serif;
  }
  .letterhead {
    position: absolute;
    left: 197px;
    top: 30px;
    width: 806px;
    height: 1140px;
    background: var(--paper);
    overflow: hidden;
  }
  .header-band {
    position: absolute;
    left: 0;
    top: 0;
    width: 430px;
    height: 126px;
  }
  .brand {
    position: absolute;
    left: 21px;
    top: 38px;
    display: flex;
    align-items: center;
    gap: 14px;
  }
  .brand-dot {
    width: 44px;
    height: 44px;
    border-radius: 50%;
    background: var(--paper);
  }
  .brand-name {
    color: var(--paper);
    font-size: 50px;
    font-weight: 400;
    line-height: 1;
    letter-spacing: 0.5px;
  }
  .backdrop-field {
    position: absolute;
    left: -229px;
    top: 203px;
    width: 730px;
    height: 730px;
    border-radius: 50%;
    background: var(--tint);
  }
  .corner-field {
    position: absolute;
    left: 610px;
    top: 755px;
    width: 392px;
    height: 392px;
    border-radius: 50%;
    background: var(--tint-strong);
  }
  .date {
    position: absolute;
    left: 554px;
    top: 197px;
    font-size: 14px;
    font-weight: 500;
    color: var(--ink);
  }
  .headline {
    position: absolute;
    left: 111px;
    top: 211px;
    margin: 0;
    font-size: 23px;
    font-weight: 700;
    letter-spacing: 1px;
    color: var(--ink);
  }
  .sender-name {
    position: absolute;
    left: 109px;
    top: 819px;
    font-family: "Lobster", cursive;
    font-size: 21px;
    color: var(--accent);
  }
  .sender-role {
    position: absolute;
    left: 109px;
    top: 845px;
    font-size: 13px;
    font-weight: 500;
    color: var(--ink);
  }
  .signature-area {
    position: absolute;
    left: 91px;
    top: 891px;
    width: 231px;
    height: 98px;
    border-radius: 6px;
    background: var(--tint-strong);
    opacity: 0.6;
  }
  .company-details {
    position: absolute;
    left: 108px;
    top: 1007px;
    margin: 0;
    font-size: 13.4px;
    font-weight: 500;
    line-height: 16.4px;
    color: var(--text);
    font-style: normal;
    white-space: nowrap;
  }
</style>
</head>
<body>
  <main class="letterhead">
    <div class="backdrop-field" role="img" aria-label="Soft grey decorative dot field"></div>
    <div class="corner-field" role="img" aria-label="Large faint decorative corner graphic"></div>

    <svg class="header-band" viewBox="0 0 430 126" aria-hidden="true">
      <polygon points="0,0 430,0 306,126 0,126" fill="var(--band)"/>
    </svg>
    <div class="brand">
      <span class="brand-dot"></span>
      <span class="brand-name">VOLTRINA</span>
    </div>

    <div class="date">Date: xx / xx / xxxx</div>
    <h1 class="headline">Headline</h1>

    <div class="sender-name">Your Name</div>
    <div class="sender-role">LOREM IPSUM</div>
    <div class="signature-area" role="img" aria-label="Handwritten signature"></div>

    <address class="company-details">
      VAT TAX DE5704168<br>
      Norrfeld Bank IBAN DE421705238ß310482<br>
      KOLV3154802 EORI 3041296587<br>
      HRB 61508<br>
      Adress: VOLTRINA UG Amsel Strasse 7 Postal Code 04683<br>
      City Harzwalde Germany<br>
      Email: info@voltrina-example.com
    </address>
  </main>
</body>
</html>
```